Game, Voice & Dedicated Server Company Needs a Business Card Design

We need a new business card design, centered around our new logo (PSD provided below).

Designs that we do like:
https://plomvaste.net/item/corporate-business-card/5382047?s_rank=31 (needs to be made more eye catching)

Our main areas of business are:
- Dedicated Servers
- Game Servers
- Voice Servers
- Mitigation Security Specialists

Industry/Entity Type

Business

Contact Information for Business Card

On the card: (and anything else you would suggest)
- Staff member name
- Staff member position in company
- Staff member phone number
- Staff member email
- Other / Staff member Skype
- Website link

Colors
9bcb3c
abd036

Requirements
Must have
• Design of Card:
• - Green (same green as the logo)
• - Business / Corporate design
• - Something a little different / abstract that shouts premium

```html
<!DOCTYPE html>
<html lang="en">
<head>
<meta charset="UTF-8">
<title>Brightwave Hosting – Business Cards</title>
<link href="https://fonts.googleapis.com/css2?family=Montserrat:wght@400;500;700&display=swap" rel="stylesheet">
<style>
  :root{
    --green:#8cc63f;
    --green-dark:#7ab32e;
    --grey:#7d7d80;
    --ink:#1e1e1e;
    --white:#ffffff;
    --backdrop:#2b2b2d;
  }
  *{box-sizing:border-box;margin:0;padding:0}
  html,body{width:1200px;height:900px;overflow:hidden}
  body{background:var(--backdrop);font-family:"Montserrat",sans-serif;position:relative}

  .card{position:absolute;width:560px;height:320px;border-radius:20px;overflow:hidden;background:var(--white);box-shadow:0 18px 40px rgba(0,0,0,.45)}
  .card--back{left:110px;top:110px}
  .card--front{left:530px;top:470px}

  /* back side */
  .brand-mark{position:absolute;left:0;right:0;top:70px;display:flex;align-items:center;justify-content:center;gap:14px}
  .brand-mark__dot{width:38px;height:38px;border-radius:50%;background:var(--green)}
  .brand-mark__name{font-weight:700;font-size:30px;letter-spacing:1px;color:var(--green);text-transform:uppercase}
  .services{position:absolute;left:0;right:0;top:170px;text-align:center;font-size:15px;line-height:21px;color:var(--ink);font-weight:500}
  .services__rule{width:300px;height:2px;background:var(--green);margin:8px auto 6px}
  .services__web{font-size:16px}
  .services__web span{color:var(--green)}

  /* front side */
  .front-art{position:absolute;inset:0}
  .brand-vertical{position:absolute;left:22px;top:20px;width:140px;height:280px}
  .brand-vertical__name{position:absolute;left:50%;top:118px;transform:translate(-50%,-50%) rotate(-90deg);white-space:nowrap;font-weight:700;font-size:27px;line-height:30px;color:var(--green);text-transform:uppercase;text-align:left}
  .brand-vertical__dot{position:absolute;left:50%;bottom:14px;transform:translateX(-50%);width:42px;height:42px;background:var(--green)}

  .person{position:absolute;left:232px;top:92px;color:var(--white)}
  .person__name{font-weight:700;font-size:27px;letter-spacing:.5px}
  .person__role{font-size:13px;margin-top:2px;margin-left:14px}
  .contacts{position:absolute;left:246px;top:168px;list-style:none;color:var(--white);font-size:14px;line-height:23px}
  .contacts li{display:flex;align-items:center;gap:10px}
  .contacts svg{width:11px;height:11px;flex:none}
</style>
</head>
<body>

  <section class="card card--back" aria-label="Card back">
    <div class="brand-mark">
      <span class="brand-mark__dot"></span>
      <span class="brand-mark__name">Brightwave Hosting</span>
    </div>
    <div class="services">
      <p>Dedicated Servers - Game Servers</p>
      <p>Voice Servers - Business relations</p>
      <div class="services__rule"></div>
      <p class="services__web">www.<span>brightwavehosting</span>.com</p>
    </div>
  </section>

  <section class="card card--front" aria-label="Card front">
    <svg class="front-art" viewBox="0 0 560 320" aria-hidden="true">
      <polygon points="194,0 560,0 560,320 194,320 194,134 176,118 194,102" fill="var(--green)"/>
      <polyline points="184,0 184,98 168,118 184,138 184,320" fill="none" stroke="var(--grey)" stroke-width="3"/>
    </svg>

    <div class="brand-vertical">
      <p class="brand-vertical__name">Brightwave<br>Hosting</p>
      <span class="brand-vertical__dot"></span>
    </div>

    <div class="person">
      <p class="person__name">Marten Olsby</p>
      <p class="person__role">Director</p>
    </div>

    <ul class="contacts">
      <li>
        <svg viewBox="0 0 12 12"><path d="M2.5 1 L4.5 1 L5 3.5 L3.8 4.4 C4.5 6 6 7.5 7.6 8.2 L8.5 7 L11 7.5 L11 9.5 C11 10.3 10.3 11 9.5 11 C5 11 1 7 1 2.5 C1 1.7 1.7 1 2.5 1Z" fill="#fff"/></svg>
        +330 4815-2093
      </li>
      <li>
        <svg viewBox="0 0 12 12"><rect x="1" y="2.5" width="10" height="7" fill="none" stroke="#fff" stroke-width="1.2"/><polyline points="1,2.5 6,6.5 11,2.5" fill="none" stroke="#fff" stroke-width="1.2"/></svg>
        info@brightwavehosting.com
      </li>
      <li>
        <svg viewBox="0 0 12 12"><circle cx="6" cy="6" r="4.5" fill="#fff"/></svg>
        @brightwavehosting
      </li>
      <li>
        <svg viewBox="0 0 12 12"><circle cx="6" cy="6" r="4.8" fill="none" stroke="#fff" stroke-width="1.1"/><ellipse cx="6" cy="6" rx="2" ry="4.8" fill="none" stroke="#fff" stroke-width="1"/><line x1="1.2" y1="6" x2="10.8" y2="6" stroke="#fff" stroke-width="1"/></svg>
        www.brightwavehosting.com
      </li>
    </ul>
  </section>

</body>
</html>
```